Web Design Project - Do It Yourself Website/Blog company

Task Description:
We need a new website for Brellwick.com, an established company that has been around for 10+ years.
Our website is fine, but we believe more is possible.
We are seeking a new look and feel, as well as a new "sales message". We're not sure that visitors to our site immediately understand what we do, and how we are positioned.
We are looking for a new design (including the major text on the pages), for the principal webpages. The physical implementation we can handle.
Our product is do-it-yourself websites and blogs, for home users and small business.
Our system is widget based, with powerful tools and widgets that provide features well beyond "just a website." For instance, we provide all of the mailing list management, security, hosting, and powerful widgets like shopping, discussion forums, payment buttons, etc. Our mission is to put the powerful tools, normally available only on websites costing tens of thousands of dollars, and make them available to people who know nothing about web design, and don't want to learn.
The price for our product begins at “Free” for a website or blog with good functionality but limited storage. For $3 a month, we provide a more robust product including a personalized URL/Domain, more storage and additional tools and for $10 a month customers get a very robust system including outbound email and newsletter capabilities and powerful search engine optimization tools.
The overall goal of the website is to solicit people to sign-up for a free website. Doing so requires no credit card or other obligation, though the customer does need to provide some limited contact information and agree to our EULA.
Our current website is at www.brellwick.com, but we encourage prospective designers to disregard any information they find there directly associated with the product capabilities. We are open and eager to move forward in a new and fresh design direction.
Must have features:
The goal is signup for a free website, so a clear path into the sign-up process is paramount.
Ultimately our goal is to get users who will benefit from our services enough to pay at least $3 a month for services, so a product that targets people with specific needs that they are willing to pay for (businesses/enthusiasts) over casual users (children/teen) is needed.
Target Market: Our core users are small-to-medium sized businesses – usually sole proprietors who are very hands on. We also have a large base of affluent enthusiasts who engage in boating, breeding (dogs/horses), and casual activities. We also have some amateur sports teams, personal family websites and general consumer traffic.
Scope of project: We're looking for the key pages on the site, the wording for the key points on each of the principal pages, and the overall look/feel. We want something that communicates clearly what we do, and why customers should try our product.
Delivery: We're ok with any type of delivery of the finished product. The site can be mocked up in powerpoint, photoshop, or HTML - whatever. We're looking for a site we would want to buy from, that communicates succinctly and clearly what we do, and why we are the best (or, at a minimum takes away the fear of giving us a try). Once we have this, we are open to contracting you to do the physical html implementation, but see this as a seperate project.
Updates
Reason: I haven't seen any designs yet that seemed different enough from what I have to excite me.
To motivate designers, and simplify the project, let's take this approach:
- I only need the homepage (Originally, I was asking for a few pages)
- I'm happy with submission in any format
- Your design doesn't need to have all of the copy. You can greek the small print. I just want to see the overall look, and sales messsage (images, headlines, and section headers). Give me enough that I can easily envision the finished product
Important: As soon as I see any design that interests me, I'll make the money non-refundable
Dale M Brellwick.com
I've just made the money non-refundable, so someone is going to get a payday.
This is the feedback I gave on the most recent design:
"...On the right track. I like this. Best so far.
My only comments:
- A subset of our product is free, so I don't like to say "Try it now", because most users are in fact paying nothing, and yet getting tremendous value.
- We should reference that it is "websites and blogs" .. not just websites.
- If you find a place to put it, we could/should(?) mention three things that might lend credibility to us: 1) In business since 1999, 2) Built over 100,000 websites, 3) My background (Founder/CEO Quillfen Digital, leading consumer software company)
Thank you!
Dale Morrow
PS I am making the money non-refundable. You are in the lead....
Target Market(s)
Small business (under 10 employees)
Homeowners Associations
Owner's groups
Clubs
Music groups
People with expensive assets they want a website for (boats, second homes)
Industry/Entity Type
Credit Card
Requirements
Must have
- Compelling visual impact
Sales message that communicates why we are the best option (ease of use?, low cost? Power?)
Copy examples (Section headings, and enough text for each section that we can tell what the sales message is)
Should not have
- We want something that makes us look amazing!

```html
<!DOCTYPE html>
<html lang="en">
<head>
<meta charset="utf-8">
<title>Brellwick – Easy Website Building & Host Company</title>
<link href="https://fonts.googleapis.com/css2?family=Dosis:wght@500;600&family=Ubuntu:wght@300;400;500&display=swap" rel="stylesheet">
<style>
:root{
  --blue:#0e5ba8;
  --blue-dark:#0a4689;
  --blue-deep:#0b3f86;
  --blue-light:#1f7fd0;
  --heading:#1b6fbf;
  --text:#555;
  --text-soft:#666;
  --rule:#dcdcdc;
  --band:#f1f1f1;
  --white:#fff;
}
*{margin:0;padding:0;box-sizing:border-box}
html,body{width:885px;height:1200px;overflow:hidden;background:var(--white)}
body{position:relative;font-family:"Ubuntu",sans-serif;color:var(--text)}
.header{position:absolute;top:0;left:0;width:885px;height:105px;border-top:5px solid #eee}
.brand{position:absolute;left:40px;top:32px;display:flex;align-items:center;gap:8px}
.brand-square{width:40px;height:40px;background:var(--blue);border-radius:6px}
.brand-name{font-family:"Dosis",sans-serif;font-weight:500;font-size:31px;color:#4a6f95;line-height:1}
.brand-tag{font-family:"Dosis",sans-serif;font-size:10px;color:#4a6f95;letter-spacing:.5px;margin-top:2px}
.nav{position:absolute;right:0;top:53px;display:flex}
.nav a{font-family:"Dosis",sans-serif;font-weight:500;font-size:14px;color:#4a5a6a;text-decoration:none;padding:14px 17px 12px;border-left:1px solid var(--rule)}
.nav a:first-child{border-left:none}
.hero{position:absolute;top:105px;left:0;width:885px;height:337px;background:linear-gradient(90deg,var(--blue-deep),var(--blue-light) 55%,var(--blue) 100%);color:var(--white)}
.hero h1{position:absolute;left:53px;top:28px;font-family:"Dosis",sans-serif;font-weight:600;font-size:32px;line-height:1.1}
.hero h1 span{display:block;font-size:25px;margin-top:6px}
.hero .lead{position:absolute;left:51px;top:107px;font-size:16px;font-weight:300}
.ticks{position:absolute;left:64px;top:138px;list-style:none;width:290px}
.ticks li{font-size:11.5px;font-weight:300;padding:4px 0 4px 19px;border-bottom:1px solid rgba(255,255,255,.12);position:relative;white-space:nowrap}
.ticks li svg{position:absolute;left:0;top:7px}
.cta{position:absolute;left:80px;top:260px;background:var(--white);color:var(--heading);font-family:"Dosis",sans-serif;font-weight:600;font-size:14px;padding:8px 12px;border-radius:4px;box-shadow:0 2px 4px rgba(0,0,0,.25)}
.cta-note{position:absolute;left:207px;top:280px;font-family:"Dosis",sans-serif;font-size:11px}
.showcase{position:absolute;left:448px;top:27px;width:402px;height:278px;border-radius:8px;background:linear-gradient(180deg,#2a2a2a 0 86%,#d8d8d8 86%)}
.showcase-screen{position:absolute;left:14px;top:12px;right:14px;height:224px;background:radial-gradient(circle at 50% 55%,#e9f1fa,#8fb6dd 55%,#ffffff 80%)}
.stand{position:absolute;left:585px;top:410px;width:112px;height:55px;background:linear-gradient(180deg,#cfcfcf,#f2f2f2);clip-path:polygon(25% 0,75% 0,100% 100%,0 100%);border-radius:4px}
.features{position:absolute;top:442px;left:0;width:885px;height:325px;background:linear-gradient(180deg,#fff,#f3f3f3 48%,#fff 50%,#f3f3f3)}
.features .hr{position:absolute;left:0;top:177px;width:885px;height:1px;background:var(--rule)}
.vr{position:absolute;top:30px;height:280px;border-left:1px dotted #ccc}
.feature{position:absolute;width:260px}
.feature .icon{position:absolute;left:0;top:0;width:44px;height:44px;border-radius:50%}
.feature h2{margin-left:54px;font-family:"Dosis",sans-serif;font-weight:500;font-size:22px;color:var(--heading);line-height:1.2}
.feature p{margin-left:55px;font-size:11px;font-weight:300;color:var(--text);line-height:1.45;margin-top:4px}
.more{display:inline-block;margin:10px 0 0 55px;font-size:10.5px;color:#777;padding:4px 8px;border:1px solid #ddd;border-radius:3px;background:var(--white)}
.section-title{position:absolute;font-family:"Dosis",sans-serif;font-weight:500;font-size:18px;color:#555}
.title-rule{position:absolute;height:1px;background:var(--rule)}
.links{position:absolute;list-style:none}
.links li{font-size:10px;color:#555;margin-bottom:11px;padding-left:10px;position:relative;line-height:1.3}
.links li::before{content:"›";position:absolute;left:0;top:-1px;color:#999}
.partners{position:absolute;top:1010px;left:0;width:885px;height:92px;background:var(--band);display:flex;align-items:center;justify-content:space-around;padding:0 20px}
.partner{font-size:14px;font-weight:500;color:#5a6a7a;display:flex;align-items:center;gap:5px}
.partner i{display:inline-block;width:12px;height:12px;background:#7a8a9a}
.badge{width:80px;height:30px;border-radius:4px}
.footer{position:absolute;top:1110px;left:0;width:885px;height:90px;background:var(--blue-dark);color:var(--white);font-size:10px}
.footer .links-row{position:absolute;left:20px;top:24px}
.footer .links-row span{margin:0 6px;opacity:.7}
.footer .copy{position:absolute;left:17px;top:50px}
.footer .social{position:absolute;right:52px;top:15px;display:flex;align-items:center;gap:6px;font-size:11px}
.footer .social b{width:26px;height:26px;border-radius:50%;background:var(--white);display:inline-block}
.footer .social em{font-style:normal;margin-right:8px}
</style>
</head>
<body>
<header class="header">
  <div class="brand">
    <div class="brand-square"></div>
    <div><div class="brand-name">BRELLWICK</div><div class="brand-tag">WEB &amp; EMAIL MARKETING SERVICES</div></div>
  </div>
  <nav class="nav"><a>About Brellwick</a><a>Our Product</a><a>Services</a><a>Testimonials</a><a>Log In</a></nav>
</header>

<section class="hero">
  <h1>Easy Website Building<span>&amp; Host Company</span></h1>
  <p class="lead">Create your Website or Blog in Minutes.</p>
  <ul class="ticks">
    <li><svg width="11" height="9" viewBox="0 0 11 9"><path d="M1 5l3 3 6-7" fill="none" stroke="#fff" stroke-width="1.8"/></svg>Easy drag &amp; drop interface.</li>
    <li><svg width="11" height="9" viewBox="0 0 11 9"><path d="M1 5l3 3 6-7" fill="none" stroke="#fff" stroke-width="1.8"/></svg>No programming skills needed.</li>
    <li><svg width="11" height="9" viewBox="0 0 11 9"><path d="M1 5l3 3 6-7" fill="none" stroke="#fff" stroke-width="1.8"/></svg>Includes your world class hosting &amp; web address.</li>
    <li><svg width="11" height="9" viewBox="0 0 11 9"><path d="M1 5l3 3 6-7" fill="none" stroke="#fff" stroke-width="1.8"/></svg>Affordable pricing for Consumers &amp; Business.</li>
    <li><svg width="11" height="9" viewBox="0 0 11 9"><path d="M1 5l3 3 6-7" fill="none" stroke="#fff" stroke-width="1.8"/></svg>Powerful design tools including Image &amp; Text Editors.</li>
  </ul>
  <div class="cta">GET STARTED ›</div>
  <div class="cta-note">Try it free Today</div>
  <div class="showcase"><div class="showcase-screen" role="img" aria-label="Illustration of website templates bursting through a desktop monitor screen"></div></div>
</section>
<div class="stand"></div>

<section class="features">
  <div class="hr"></div>
  <div class="vr" style="left:293px"></div>
  <div class="vr" style="left:586px"></div>

  <div class="feature" style="left:33px;top:38px">
    <div class="icon" role="img" aria-label="Envelope icon" style="background:#f2c04a"></div>
    <h2>Grow Your Business</h2>
    <p>Email Marketing Suite, send<br>newsletters, announcements<br>and track every email.</p>
    <span class="more">READ MORE</span>
  </div>
  <div class="feature" style="left:337px;top:38px">
    <div class="icon" role="img" aria-label="Magnifying glass icon" style="background:#b9d3ee"></div>
    <h2>Get Found Today</h2>
    <p>Build your brand and drive traffic<br>with Search Engine Tools.</p>
    <span class="more">READ MORE</span>
  </div>
  <div class="feature" style="left:618px;top:38px">
    <div class="icon" role="img" aria-label="Help question mark icon" style="background:#1c66c4"></div>
    <h2>Need Help?</h2>
    <p>Visit our Online Help Center,<br>Quick Reference Guides, FAQ,<br>Webinars and more!</p>
    <span class="more">READ MORE</span>
  </div>

  <div class="feature" style="left:29px;top:192px">
    <div class="icon" role="img" aria-label="Shopping basket icon" style="background:#f0c233"></div>
    <h2>Shopping Made Easy</h2>
    <p>Simple to use ecommerce tools<br>and buttons to collect money.</p>
    <span class="more">READ MORE</span>
  </div>
  <div class="feature" style="left:340px;top:192px">
    <div class="icon" role="img" aria-label="Globe icon" style="background:#2d6cc0"></div>
    <h2>Explore</h2>
    <p>Explore some of the thousands<br>of websites we've helped create<br>in our over 10 years of business</p>
    <span class="more">READ MORE</span>
  </div>
  <div class="feature" style="left:627px;top:192px">
    <div class="icon" role="img" aria-label="House icon" style="background:#b8b8b8"></div>
    <h2>Stay Connected</h2>
    <p>Download Brellwick Connect our<br>Mobile App.</p>
    <span class="more">READ MORE</span>
  </div>
</section>

<h3 class="section-title" style="left:25px;top:797px">Products &amp; Features</h3>
<div class="title-rule" style="left:25px;top:823px;width:640px"></div>
<h3 class="section-title" style="left:690px;top:797px">Help &amp; Support</h3>
<div class="title-rule" style="left:690px;top:823px;width:175px"></div>

<ul class="links" style="left:25px;top:837px"><li>Custom Menus</li><li>Text Editing Tools</li><li>Image Editing Tools</li><li>Photo Galleries</li><li>Blogging Tools</li></ul>
<ul class="links" style="left:140px;top:837px"><li>Social Media Sharing</li><li>Music, Video &amp; Documents</li><li>Mapline &amp; Skycast Weather</li><li>Forum, Scheduling &amp; Calendar</li></ul>
<ul class="links" style="left:326px;top:837px;width:160px"><li>RSS, Comments &amp; Sign In</li><li>Payment &amp; Shopping Tools</li><li>Polls, Surveys and Forms</li><li>Real Estate Listing &amp; Mortgage Calculator</li><li>JavaScript, Contact Lists &amp; Contact Details</li></ul>
<ul class="links" style="left:510px;top:838px"><li>Search &amp; Sign Up/Register</li><li>Custom Domain Names</li><li>Search Engine Tools</li><li>Email Marketing Suite</li><li>Ecommerce Tools</li></ul>
<ul class="links" style="left:690px;top:837px"><li>Webinars</li><li>User Group Forum</li><li>Quick Start Guide</li><li>FAQ</li><li>Email Support</li></ul>

<h3 class="section-title" style="left:21px;top:985px">Our Partners</h3>
<div class="partners">
  <span class="partner">Yonderly</span>
  <span class="partner">Blipseek</span>
  <span class="partner"><i></i>Aurelon</span>
  <span class="badge" role="img" aria-label="Verified and secured badge" style="background:#2d4f8c"></span>
  <span class="partner">Chirpwell</span>
  <span class="badge" role="img" aria-label="Partner badge" style="background:#1d4a8f;width:84px;height:32px"></span>
  <span class="badge" role="img" aria-label="Secure web site badge" style="background:#9aa86a"></span>
  <span class="partner"><i style="border-radius:50%"></i>Corvana</span>
</div>

<footer class="footer">
  <div class="links-row">Affiliate Program<span>|</span>Privacy Policy<span>|</span>Contact Us<span>|</span>Log In<span>|</span>Terms of Service</div>
  <div class="copy">© 2012 Company Name &nbsp;|&nbsp; All right reserved</div>
  <div class="social"><em>Stay Connect</em><b role="img" aria-label="Friendfold"></b><b role="img" aria-label="Chirpwell"></b></div>
</footer>
</body>
</html>
```